Process Flow Chart for Real Estate Agency

We need a visual flow chart of the process of selling a home for our Real Estate Agency. This visual will be provided to all new staff to explain the process and also to potential clients to explain how detailed the process is. It needs to show each step as detailed in the attached word doc and use icons and arrows to show the direction of flow.

Target Market(s)

Staff & Potential Clients

Industry/Entity Type

Real Estate

Font styles to use
Sans Serif

Colors

Designer to choose colors to be used in the design.

Requirements
Must have
• Easy to read, lots of icons, colour coded with Agent in one colour, Admin in another (some tasks are either/or so not sure what to colour those ones.)
Nice to have
• Include one of the two attached logos

```html
<!DOCTYPE html>
<html lang="en">
<head>
<meta charset="utf-8">
<title>Harborlane Real Estate – Listing Process Flow</title>
<link href="https://fonts.googleapis.com/css2?family=Montserrat:wght@400;500;700&display=swap" rel="stylesheet">
<style>
  :root{
    --backdrop:#1c2b2c;
    --paper:#efefed;
    --slate:#5d6d75;
    --slate-dark:#46555c;
    --ink:#4c5a61;
    --yellow:#f3cd1c;
    --white:#ffffff;
  }
  *{margin:0;padding:0;box-sizing:border-box}
  html,body{width:1200px;height:632px;overflow:hidden;background:var(--backdrop);font-family:'Montserrat',sans-serif}
  .spread{position:absolute;left:30px;top:114px;width:1140px;height:404px;display:flex;box-shadow:0 18px 40px rgba(0,0,0,.45)}
  .page{position:relative;width:570px;height:404px;background:var(--paper);overflow:hidden}
  .page--left{background:linear-gradient(90deg,var(--paper) 88%,#dcdcd9 100%)}
  .page--right{background:linear-gradient(90deg,#dcdcd9 0%,var(--paper) 10%)}
  .page svg{position:absolute;left:0;top:0}
  .brand{position:absolute;display:flex;align-items:center;gap:6px;color:var(--slate-dark);font-weight:700;font-size:13px;letter-spacing:-.2px;line-height:1.1}
  .brand__dot{width:14px;height:14px;border-radius:50%;background:var(--yellow)}
  .brand small{display:block;font-weight:700;font-size:7px;letter-spacing:.5px;color:var(--slate-dark)}
  .page--left .brand{left:26px;top:62px}
  .page--right .brand{right:26px;top:26px}
  .steps{position:absolute;left:342px;top:46px;width:214px;list-style:none}
  .steps li{position:relative;padding-left:12px;margin-bottom:5px;font-size:7px;line-height:1.25;color:var(--ink)}
  .steps li::before{content:"";position:absolute;left:0;top:2px;width:6px;height:6px;border-radius:50%;border:1.3px solid var(--slate)}
  .steps b{display:block;font-size:8.5px;font-weight:700;color:var(--slate-dark)}
  .folio{position:absolute;bottom:46px;width:30px;height:18px;background:var(--slate);color:var(--white);font-size:9px;font-weight:700;display:flex;align-items:center;justify-content:center}
  .page--left .folio{right:22px}
  .page--right .folio{left:22px}
  .node-text{font-size:5.6px;fill:var(--ink)}
  .node-title{font-size:6.8px;font-weight:700;fill:var(--slate-dark)}
  .tab-text{font-size:6.6px;font-weight:700;fill:var(--white)}
  .note{font-size:6.3px;fill:var(--ink)}
  .bottom-title{font-size:7.4px;font-weight:700;fill:var(--slate-dark)}
</style>
</head>
<body>
<main class="spread">

  <!-- Page 01 -->
  <section class="page page--left">
    <svg width="570" height="404" viewBox="0 0 570 404">
      <polygon points="270,34 570,20 570,28 270,42" fill="var(--slate)"/>
      <polygon points="0,372 570,330 570,334 0,376" fill="var(--slate)" opacity=".85"/>
      <polygon points="0,390 300,370 300,376 0,398" fill="var(--yellow)"/>

      <g fill="none" stroke="var(--slate)" stroke-width="3">
        <path d="M45 162 V190 H300 V162"/>
        <path d="M75 190 V223 M160 190 V223 M245 190 V223"/>
      </g>

      <g fill="var(--paper)" stroke="var(--slate)" stroke-width="3">
        <circle cx="45" cy="140" r="22"/>
        <circle cx="130" cy="140" r="22"/>
        <circle cx="215" cy="140" r="22"/>
        <circle cx="300" cy="140" r="22"/>
        <circle cx="245" cy="245" r="22"/>
      </g>
      <g fill="var(--slate)">
        <circle cx="75" cy="245" r="22"/>
        <circle cx="160" cy="245" r="22"/>
        <circle cx="75" cy="310" r="22"/>
        <circle cx="160" cy="310" r="22"/>
        <circle cx="245" cy="310" r="22"/>
      </g>

      <g fill="var(--slate-dark)">
        <path d="M84 136 l6 4 -6 4z"/><path d="M169 136 l6 4 -6 4z"/><path d="M254 136 l6 4 -6 4z"/>
        <path d="M114 241 l6 4 -6 4z"/><path d="M199 241 l6 4 -6 4z"/>
        <path d="M114 306 l6 4 -6 4z"/><path d="M199 306 l6 4 -6 4z"/>
      </g>

      <!-- icons -->
      <g stroke="var(--slate)" stroke-width="2.2" fill="none" stroke-linecap="round" stroke-linejoin="round">
        <circle cx="45" cy="138" r="6"/><path d="M35 140 a10 10 0 0 1 20 0 M37 150 h16"/>
        <path d="M121 140 l6 6 12 -13"/>
        <path d="M204 142 l7 -6 7 4 7 -4 M206 142 l6 5 4 -2 5 3"/>
        <rect x="290" y="132" width="20" height="17" rx="2"/><path d="M290 138 h20 M295 129 v5 M305 129 v5"/>
        <path d="M236 245 l6 6 12 -13"/>
      </g>
      <g stroke="var(--white)" stroke-width="2" fill="none" stroke-linecap="round">
        <rect x="152" y="234" width="16" height="22" rx="1"/><path d="M156 240 h8 M156 245 h8 M156 250 h6"/>
        <ellipse cx="75" cy="302" rx="10" ry="3.5"/><path d="M65 302 v14 a10 3.5 0 0 0 20 0 v-14 M65 309 a10 3.5 0 0 0 20 0"/>
        <rect x="148" y="304" width="14" height="10"/><path d="M162 307 h6 l4 4 v3 h-10"/><circle cx="153" cy="317" r="2"/><circle cx="167" cy="317" r="2"/>
        <circle cx="242" cy="307" r="7"/><path d="M247 312 l6 6"/>
      </g>
      <path d="M62 237 h26 v14 h-18 l-6 5 v-5 h-2z" fill="var(--white)"/>
      <text x="75" y="247" text-anchor="middle" font-size="7" font-weight="700" fill="var(--slate)">SMS</text>
    </svg>

    <div class="brand"><span class="brand__dot"></span><div>Harborlane<small>REAL ESTATE</small></div></div>

    <ul class="steps">
      <li><b>Agent Calls Potential Client</b>to arrange a time to meet and obtain details about the property</li>
      <li><b>Agent Ensures</b>all decision makers will be present at meeting</li>
      <li><b>Agent Adds Vendors</b>contact details on phone</li>
      <li><b>Agent Adds Appointment</b>to personal calendar</li>
      <li><b>Agent Sends SMS</b>to potential client to thank them for the opportunity</li>
      <li><b>Agent/ Admin Orders</b>ARE from Ellworth's</li>
      <li><b>Agent Completes a TMP</b>to provide to Admin for Prelisting kit prep</li>
      <li><b>Admin Prepares</b>pre-listing kit with questionnaire, sample brochure &amp; cover letter, property magazine, agent profile booklet</li>
      <li><b>Admin/ Agent Delivers</b>pre-listing kit (preferably within the hour) &amp; SMS potential vendor</li>
      <li><b>Admin/ Agent to Research</b>&amp; prints comparable Sales reports</li>
    </ul>
    <div class="folio">01</div>
  </section>

  <!-- Page 02 -->
  <section class="page page--right">
    <svg width="570" height="404" viewBox="0 0 570 404">
      <polygon points="0,78 300,48 300,56 0,86" fill="var(--slate)"/>
      <polygon points="0,318 460,295 460,301 0,324" fill="var(--slate)" opacity=".85"/>
      <polygon points="460,293 570,287 570,295 460,301" fill="var(--yellow)"/>

      <!-- connectors -->
      <g fill="none" stroke="var(--slate)" stroke-width="2">
        <path d="M128 105 H190 L220 104"/>
        <path d="M110 155 H170 L195 180"/>
        <path d="M118 205 H170 L190 205"/>
        <path d="M110 253 H268"/>
        <path d="M448 71 H400 L378 80"/>
        <path d="M448 123 L430 132"/>
        <path d="M448 161 L430 153"/>
        <path d="M448 205 L420 210"/>
      </g>
      <circle cx="300" cy="170" r="60" fill="none" stroke="var(--slate)" stroke-width="1" stroke-dasharray="2 2"/>

      <!-- hub -->
      <g fill="var(--slate)">
        <circle cx="300" cy="170" r="16"/>
        <circle cx="300" cy="135" r="9"/><circle cx="330" cy="152" r="9"/><circle cx="330" cy="188" r="9"/>
        <circle cx="300" cy="205" r="9"/><circle cx="270" cy="188" r="9"/><circle cx="270" cy="152" r="9"/>
      </g>
      <g stroke="var(--white)" stroke-width="1.4" fill="none" stroke-linecap="round">
        <circle cx="294" cy="168" r="3"/><circle cx="306" cy="168" r="3"/><path d="M288 178 a6 5 0 0 1 12 0 M300 178 a6 5 0 0 1 12 0"/>
        <path d="M296 135 l3 3 5 -6"/>
        <rect x="325" y="148" width="10" height="8"/>
        <path d="M325 188 h10 M330 183 v10"/>
        <circle cx="299" cy="204" r="3"/><path d="M301 206 l3 3"/>
        <rect x="266" y="183" width="8" height="10"/>
        <path d="M265 152 h10 M265 155 h7"/>
      </g>

      <!-- petals -->
      <g fill="var(--paper)" stroke="var(--slate)" stroke-width="2">
        <circle cx="252" cy="102" r="36"/>
        <circle cx="345" cy="86" r="36"/>
        <circle cx="400" cy="142" r="36"/>
        <circle cx="392" cy="218" r="36"/>
        <circle cx="300" cy="252" r="36"/>
        <circle cx="222" cy="196" r="36"/>
      </g>
      <g text-anchor="middle">
        <text><tspan class="node-title" x="252" y="84">Admin</tspan><tspan class="node-title" x="252" dy="7">Prepares</tspan><tspan class="node-text" x="252" dy="7">written appraisal</tspan><tspan class="node-text" x="252" dy="6.5">report hand-</tspan><tspan class="node-text" x="252" dy="6.5">deliver with</tspan><tspan class="node-text" x="252" dy="6.5">coffee vouchers</tspan><tspan class="node-text" x="252" dy="6.5">&amp;/or gift</tspan></text>
        <text><tspan class="node-title" x="345" y="71">Agent</tspan><tspan class="node-title" x="345" dy="7">hand-delivers</tspan><tspan class="node-text" x="345" dy="7">report with coffee</tspan><tspan class="node-text" x="345" dy="6.5">vouchers or</tspan><tspan class="node-text" x="345" dy="6.5">Corbel's</tspan><tspan class="node-text" x="345" dy="6.5">chocolates</tspan></text>
        <text><tspan class="node-title" x="400" y="127">Admin</tspan><tspan class="node-title" x="400" dy="7">Checks</tspan><tspan class="node-text" x="400" dy="7">Residential Sales</tspan><tspan class="node-text" x="400" dy="6.5">Agency &amp; enters</tspan><tspan class="node-text" x="400" dy="6.5">the listing</tspan><tspan class="node-text" x="400" dy="6.5">into CRM</tspan></text>
        <text><tspan class="node-title" x="392" y="203">Admin</tspan><tspan class="node-title" x="392" dy="7">Completes</tspan><tspan class="node-text" x="392" dy="7">the "New Listing</tspan><tspan class="node-text" x="392" dy="6.5">Checklist" and</tspan><tspan class="node-text" x="392" dy="6.5">prepares</tspan><tspan class="node-text" x="392" dy="6.5">Stock folder</tspan></text>
        <text><tspan class="node-title" x="300" y="237">Admin</tspan><tspan class="node-title" x="300" dy="7">Checks</tspan><tspan class="node-text" x="300" dy="7">for Vendor email</tspan><tspan class="node-text" x="300" dy="6.5">addresses &amp; if</tspan><tspan class="node-text" x="300" dy="6.5">required call or</tspan><tspan class="node-text" x="300" dy="6.5">SMS client</tspan></text>
        <text><tspan class="node-title" x="222" y="184">Admin</tspan><tspan class="node-title" x="222" dy="7">Completes</tspan><tspan class="node-text" x="222" dy="7">the marketing</tspan><tspan class="node-text" x="222" dy="6.5">section of</tspan><tspan class="node-text" x="222" dy="6.5">CRM</tspan></text>
      </g>

      <!-- left notes -->
      <g>
        <rect x="20" y="100" width="86" height="11" rx="5" fill="var(--slate)"/><text class="tab-text" x="26" y="108">Admin Prepares TMP</text>
        <text class="note"><tspan x="20" y="120">with Marketing Costs,</tspan><tspan x="20" dy="7">Selection booklet, Sales</tspan><tspan x="20" dy="7">Agency Agreement &amp;</tspan><tspan x="20" dy="7">Benefits Form 1</tspan></text>
        <rect x="20" y="150" width="62" height="11" rx="5" fill="var(--slate)"/><text class="tab-text" x="26" y="158">Admin Enters</text>
        <text class="note"><tspan x="20" y="170">potential Vendor into</tspan><tspan x="20" dy="7">CRM &amp; set "Appraisal" Track</tspan></text>
        <rect x="20" y="200" width="70" height="11" rx="5" fill="var(--slate)"/><text class="tab-text" x="26" y="208">Agent Confirms</text>
        <text class="note"><tspan x="20" y="220">appraisal on the</tspan><tspan x="20" dy="7">morning of the appointment</tspan><tspan x="20" dy="7">with an SMS</tspan></text>
        <rect x="20" y="248" width="58" height="11" rx="5" fill="var(--slate)"/><text class="tab-text" x="26" y="256">Agent Meets</text>
        <text class="note"><tspan x="20" y="268">with potential Vendor</tspan><tspan x="20" dy="7">and completes the appraisal</tspan></text>
      </g>

      <!-- right notes -->
      <g>
        <rect x="448" y="66" width="70" height="11" rx="5" fill="var(--slate)"/><text class="tab-text" x="454" y="74">Agent Receives</text>
        <text class="note"><tspan x="448" y="86">confirmation from vendor to</tspan><tspan x="448" dy="7">proceed with listing &amp;</tspan><tspan x="448" dy="7">arranges signing of</tspan><tspan x="448" dy="7">Sales Agency Agreement</tspan></text>
        <rect x="448" y="118" width="72" height="11" rx="5" fill="var(--slate)"/><text class="tab-text" x="454" y="126">Admin Sets Track</text>
        <text class="note"><tspan x="448" y="138">Sales Listing at date of</tspan><tspan x="448" dy="7">signing &amp; removes Appraisal</tspan></text>
        <rect x="448" y="156" width="70" height="11" rx="5" fill="var(--slate)"/><text class="tab-text" x="454" y="164">Admin Confirms</text>
        <text class="note"><tspan x="448" y="176">if Marketing has been paid</tspan><tspan x="448" dy="7">upfront &amp; prints Tax Invoice</tspan></text>
        <rect x="448" y="200" width="66" height="11" rx="5" fill="var(--slate)"/><text class="tab-text" x="454" y="208">Admin Creates</text>
        <text class="note" x="448" y="220">Property Folder in Network</text>
      </g>

      <!-- bottom steps -->
      <g fill="none" stroke="var(--slate)" stroke-width="1.3">
        <circle cx="54" cy="331" r="3"/><circle cx="54" cy="361" r="3"/>
        <circle cx="164" cy="331" r="3"/><circle cx="164" cy="373" r="3"/>
        <circle cx="312" cy="331" r="3"/><circle cx="312" cy="353" r="3"/>
        <circle cx="436" cy="331" r="3"/><circle cx="436" cy="359" r="3"/>
      </g>
      <text><tspan class="bottom-title" x="62" y="334">Admin Scans &amp; Files</tspan><tspan class="note" x="62" dy="8">Residential Sales Agency</tspan><tspan class="note" x="62" dy="7">in Network folder</tspan></text>
      <text><tspan class="bottom-title" x="62" y="364">Admin Creates OFI</tspan><tspan class="note" x="62" dy="8">Folder including digital</tspan><tspan class="note" x="62" dy="7">appraisal from ValuMetrics</tspan></text>
      <text><tspan class="bottom-title" x="172" y="334">Admin Email/Post</tspan><tspan class="note" x="172" dy="8">"Thank You For Listing" letter</tspan><tspan class="note" x="172" dy="7">with copy of Sales Agency</tspan><tspan class="note" x="172" dy="7">Agreement &amp; Seller's Guide</tspan><tspan class="note" x="172" dy="7">&amp; Marketing Tax Invoice</tspan></text>
      <text><tspan class="bottom-title" x="172" y="376">Admin Sends Form 1</tspan><tspan class="note" x="172" dy="8">Request Email through to</tspan><tspan class="note" x="172" dy="7">Ellworth Forms</tspan></text>
      <text><tspan class="bottom-title" x="320" y="334">If Auction</tspan><tspan class="note" x="320" dy="8">Agent books auctioneer</tspan></text>
      <text><tspan class="bottom-title" x="320" y="356">If Auction</tspan><tspan class="note" x="320" dy="8">Admin completes auction</tspan><tspan class="note" x="320" dy="7">day checklist and auction</tspan><tspan class="note" x="320" dy="7">day paperwork checklist</tspan></text>
      <text><tspan class="bottom-title" x="444" y="334">Agent/ Admin</tspan><tspan class="note" x="444" dy="8">creates and delivers Just</tspan><tspan class="note" x="444" dy="7">Listed letterbox drops</tspan></text>
      <text><tspan class="bottom-title" x="444" y="362">Agent to Organise</tspan><tspan class="note" x="444" dy="8">a time to have dropped off</tspan><tspan class="note" x="444" dy="7">to office or collect keys if</tspan><tspan class="note" x="444" dy="7">Vendor agrees</tspan></text>
    </svg>

    <div class="brand"><span class="brand__dot"></span><div>Harborlane<small>REAL ESTATE</small></div></div>
    <div class="folio">02</div>
  </section>

</main>
</body>
</html>
```